Modern, profession Order Insert Card for Head Shop/Smoke shop

We are looking for a modern design for our Order Insert cards where we will have some text thanking the customer for their order.
The design needs to be professional and modern, showing our logo (SVG attached) and our website URL.
Our eCommerce store sells "head shop" items, things like bongs, rolling papers, cbd products, disposable vapes, etc.
I have uploaded 2 versions of our logo, one featuring the colour of green we use across our brand, a black logo or the logo can be inverted to be a white logo on a black background.
Target Market(s)
The websites target audience is anyone needing accessories or tools to consume medicinal marijuana/the consumers favourite herbs or any one in the vaping community.
Contact Information for Business Card
Website URL, Space for a small thank you note and our logo.
Look and feel
Each slider illustrates characteristics of the customer's brand and the style your logo design should communicate.

```html
<!DOCTYPE html>
<html lang="en">
<head>
<meta charset="utf-8">
<title>Herbwayhome – Order Insert Cards</title>
<link rel="stylesheet" href="https://fonts.googleapis.com/css2?family=Fondamento&family=Playfair+Display:wght@400;700&display=swap">
<style>
  :root {
    --bg: #8fa8af;
    --card: #ffffff;
    --green: #93c440;
    --green-soft: #8dc63f;
    --green-pale: #e4efcf;
    --dark: #1e2416;
    --ink: #111111;
    --white: #ffffff;
  }
  * { margin: 0; padding: 0; box-sizing: border-box; }
  html, body { width: 1200px; height: 1200px; overflow: hidden; }
  body { background: var(--bg); position: relative; font-family: "Playfair Display", serif; }

  .insert-card {
    position: absolute;
    top: 318px;
    width: 320px;
    height: 561px;
    background: var(--card);
    overflow: hidden;
  }
  .insert-card--front { left: 212px; }
  .insert-card--back { left: 669px; }
  .card-art { position: absolute; inset: 0; width: 320px; height: 561px; }

  .thanks-title {
    position: absolute;
    left: 0; right: 0;
    top: 140px;
    text-align: center;
    font-family: "Fondamento", cursive;
    font-size: 33px;
    line-height: 1;
  }
  .thanks-note {
    position: absolute;
    left: 40px; right: 40px;
    top: 178px;
    text-align: center;
    font-size: 14.6px;
    line-height: 20.4px;
  }
  .insert-card--front .thanks-title,
  .insert-card--front .thanks-note { color: var(--green-soft); }
  .insert-card--back .thanks-title,
  .insert-card--back .thanks-note { color: var(--ink); }

  .brand-name {
    position: absolute;
    left: 0; right: 0;
    text-align: center;
    font-family: "Playfair Display", serif;
    font-weight: 700;
    font-size: 24px;
    letter-spacing: 0.5px;
  }
  .insert-card--front .brand-name { top: 482px; color: var(--white); }
  .insert-card--back .brand-name { top: 473px; color: var(--ink); }

  .brand-dot {
    position: absolute;
    left: 143px;
    top: 430px;
    width: 34px;
    height: 34px;
    border-radius: 50%;
    background: var(--green);
  }
  .brand-dot--faint {
    left: 138px;
    top: 45px;
    width: 44px;
    height: 44px;
    background: #eef3e4;
  }
</style>
</head>
<body>

  <section class="insert-card insert-card--front">
    <svg class="card-art" viewBox="0 0 320 561" aria-hidden="true">
      <defs>
        <linearGradient id="front-wash" x1="0" y1="0" x2="0" y2="1">
          <stop offset="0.25" stop-color="#ffffff"/>
          <stop offset="0.7" stop-color="#dbe9bf"/>
          <stop offset="1" stop-color="#a7d263"/>
        </linearGradient>
        <linearGradient id="front-dark" x1="0" y1="0" x2="0" y2="1">
          <stop offset="0" stop-color="#1e2416"/>
          <stop offset="0.55" stop-color="#5a7a35"/>
          <stop offset="1" stop-color="#8dc63f"/>
        </linearGradient>
      </defs>
      <rect width="320" height="561" fill="url(#front-wash)"/>
      <rect x="32" y="35" width="257" height="493" fill="none" stroke="#93c440" stroke-width="2"/>
      <path d="M0,325 C135,328 295,415 320,545 L320,561 L0,561 Z" fill="#93c440"/>
      <path d="M0,431 C70,405 150,402 210,430 C255,455 290,500 308,561 L0,561 Z" fill="url(#front-dark)"/>
      <path d="M32,424 V528 H289 V470" fill="none" stroke="#ffffff" stroke-width="2"/>
    </svg>
    <div class="brand-dot brand-dot--faint" role="img" aria-label="Faint brand emblem area"></div>
    <h2 class="thanks-title">Thank You</h2>
    <p class="thanks-note">Lorem Ipsum is simply dummy text of the printing and typesetting industry. Lorem Ipsum has been the industry's standard dummy text ever since the 1500s,</p>
    <p class="brand-name">HERBWAYHOME</p>
  </section>

  <section class="insert-card insert-card--back">
    <svg class="card-art" viewBox="0 0 320 561" aria-hidden="true">
      <rect x="31" y="32" width="258" height="494" fill="none" stroke="#93c440" stroke-width="2.5"/>
    </svg>
    <h2 class="thanks-title">Thank You</h2>
    <p class="thanks-note">Lorem Ipsum is simply dummy text of the printing and typesetting industry. Lorem Ipsum has been the industry's standard dummy text ever since the 1500s,</p>
    <div class="brand-dot"></div>
    <p class="brand-name">HERBWAYHOME</p>
  </section>

</body>
</html>
```